Brightmoor Security Solutions window graphic

Looking for a graphic for my security company , Business for the back window of my truck. Make it look cool, please.

Call now for service (206) 555-0147
Brightmoorsecuritywa.example

“ Protection you can count on”

Target Market(s)

Auto security

Industry/Entity Type

Security

```html
<!DOCTYPE html>
<html lang="en">
<head>
<meta charset="utf-8">
<title>Brightmoor Security Solutions – Rear Window Graphic</title>
<link rel="stylesheet" href="https://fonts.googleapis.com/css2?family=Michroma&display=swap">
<style>
  :root {
    --page-bg: #d9d9db;
    --glass-light: #dcdcde;
    --glass-mid: #b9babd;
    --glass-dark: #8e8f93;
    --ink: #111111;
    --accent: #e8552a;
    --accent-edge: #c9421c;
    --white: #ffffff;
  }
  html, body {
    margin: 0;
    padding: 0;
    width: 1200px;
    height: 936px;
    overflow: hidden;
    background: var(--page-bg);
  }
  .window-graphic {
    position: absolute;
    left: 50px;
    top: 290px;
    width: 1100px;
    height: 356px;
  }
  .brand-name {
    font-family: "Michroma", sans-serif;
    fill: var(--ink);
  }
  .tagline {
    font-family: "Michroma", sans-serif;
    fill: var(--white);
    font-size: 31px;
    letter-spacing: 5px;
  }
  .call-label {
    font-family: "Michroma", sans-serif;
    fill: var(--white);
    font-size: 12px;
    letter-spacing: 2px;
    font-variant: small-caps;
  }
  .phone {
    font-family: "Michroma", sans-serif;
    fill: var(--white);
    font-size: 22px;
    letter-spacing: 3px;
  }
  .web-address {
    font-family: "Michroma", sans-serif;
    fill: var(--white);
    font-size: 17px;
    letter-spacing: 3.2px;
  }
</style>
</head>
<body>
  <svg class="window-graphic" viewBox="0 0 1100 356" xmlns="http://www.w3.org/2000/svg" role="img" aria-label="Brightmoor Security Solutions rear window graphic">
    <defs>
      <radialGradient id="glassTone" cx="50%" cy="25%" r="75%">
        <stop offset="0%" stop-color="var(--glass-light)"/>
        <stop offset="60%" stop-color="var(--glass-mid)"/>
        <stop offset="100%" stop-color="var(--glass-dark)"/>
      </radialGradient>
      <clipPath id="windowShape">
        <path d="M112,5 Q556,-5 1004,5 Q1040,8 1056,40 L1096,290 Q1100,330 1080,345 L20,345 Q0,330 4,290 L44,40 Q60,8 112,5 Z"/>
      </clipPath>
    </defs>

    <g class="window-panel" clip-path="url(#windowShape)">
      <rect x="0" y="0" width="1100" height="356" fill="url(#glassTone)"/>
      <rect class="contact-strip" x="0" y="280" width="1100" height="76" fill="var(--ink)"/>
    </g>

    <line class="divider-line" x1="18" y1="234" x2="1082" y2="234" stroke="var(--ink)" stroke-width="3"/>

    <g class="brand-block">
      <rect class="brand-mark" x="538" y="92" width="40" height="40" fill="var(--ink)"/>
      <text class="brand-name" x="558" y="172" text-anchor="middle" font-size="30" letter-spacing="1">BRIGHTMOOR</text>
      <text class="brand-name" x="558" y="194" text-anchor="middle" font-size="13" letter-spacing="3">SECURITY SOLUTIONS</text>
    </g>

    <g class="tagline-band">
      <rect x="92" y="213" width="934" height="44" rx="22" fill="var(--accent)" stroke="var(--accent-edge)" stroke-width="2"/>
      <text class="tagline" x="559" y="247" text-anchor="middle">PROTECTION YOU CAN COUNT ON</text>
    </g>

    <g class="contact-details">
      <text class="call-label" x="64" y="300">Call now for service</text>
      <text class="phone" x="43" y="327">(206) 555-0147</text>
      <text class="web-address" x="1066" y="324" text-anchor="end">WWW.BRIGHTMOORSECURITYWA.EXAMPLE</text>
    </g>
  </svg>
</body>
</html>
```